Anzeigengestaltung für Teppichwäscherei
Zielgruppe
Wir sind eine Teppichwäscherei mit sitz in Recklinghausen.
Wir waschen alle arten von Teppichen vorallem hochwertige perser und designer teppiche.
Zu unserem service gehört auch die Teppichreparatur und restauration von alten und antiken stücken.
unsere zielgruppe sind private haushalte ab 40+ die auch ein teppich zuhause haben.
Aufgabenstellung
es soll modern kreative und auffällig sein aber nicht so das ältere kunden abgeschreckt sind.
folgende sachen müssen drin sein - Teppichreinigung & Teppichreparatur - Kostenlose (gratis ) Abholung und lieferung -
Format: 2sp./100mm & 3sp./100mm & 4sp./225mm
-Normalwäsche statt 19€ jetzt 16 €
-Vollwäsche statt 27€ jetzt 24 €
-Seidenwäsche statt 49€ jetzt 40 €
angebot gilt nur 5 Tage
vom xx.xx.xx bis zum xx.xx.xx

```html
<!DOCTYPE html>
<html lang="de">
<head>
<meta charset="utf-8">
<title>Teppichreinigung Anzeige</title>
<link href="https://fonts.googleapis.com/css2?family=Barlow:wght@500;600;700&display=swap" rel="stylesheet">
<style>
:root{
  --navy:#213a87;
  --navy-deep:#26337f;
  --sky:#5bc8f0;
  --paper:#ffffff;
  --strike:#d8222a;
}
*{margin:0;padding:0;box-sizing:border-box}
html,body{width:952px;height:1200px;overflow:hidden;background:var(--paper)}
body{font-family:"Barlow",Arial,sans-serif;color:var(--navy)}
.ad{position:relative;width:952px;height:1200px;overflow:hidden}
.backdrop{position:absolute;inset:0}
.headline{position:absolute;left:54px;top:40px;color:var(--paper);font-weight:700;font-size:84px;line-height:86px;letter-spacing:1px}
.subline{position:absolute;left:60px;top:218px;color:var(--paper);font-weight:700;font-size:33px;letter-spacing:.3px}
.badge{position:absolute;left:610px;top:331px;width:284px;height:284px;border-radius:50%;background:var(--navy);border:13px solid var(--paper);display:flex;flex-direction:column;align-items:center;justify-content:center;color:var(--paper);font-weight:700}
.badge-name{font-size:66px;line-height:1;letter-spacing:4px;margin-top:20px}
.badge-sub{font-size:14px;letter-spacing:2px;margin-top:16px;text-align:center;line-height:18px}
.offer{position:absolute;left:50px;height:180px}
.offer-label{position:absolute;left:0;top:0;height:86px;background:var(--navy-deep);color:var(--paper);border:5px solid var(--paper);border-radius:10px;font-weight:700;font-size:63px;line-height:74px;padding-left:30px;white-space:nowrap}
.offer-price{position:absolute;top:96px;display:flex;align-items:baseline;font-weight:700;white-space:nowrap}
.old{position:relative;font-size:37px;font-weight:600}
.old::after{content:"";position:absolute;left:0;right:14px;top:52%;height:3px;background:var(--strike);transform:rotate(-38deg)}
.jetzt{font-size:37px;font-weight:600;margin-left:6px}
.new{font-size:84px;line-height:1;margin-left:20px;letter-spacing:1px}
.validity{position:absolute;left:56px;top:1070px;font-weight:700;font-size:25px}
.footer{position:absolute;left:0;top:1111px;width:952px;height:89px;background:var(--navy-deep);border-top:6px solid var(--paper);color:var(--paper);font-size:21px;line-height:27px;font-weight:500}
.hours{position:absolute;left:32px;top:14px}
.hours b{font-weight:700}
.address{position:absolute;left:342px;top:14px}
.phone{position:absolute;left:650px;top:41px}
</style>
</head>
<body>
<div class="ad">
  <svg class="backdrop" width="952" height="1200" viewBox="0 0 952 1200">
    <defs>
      <radialGradient id="glow" cx="0.45" cy="0.45" r="0.75">
        <stop offset="0" stop-color="#ffffff"/>
        <stop offset="1" stop-color="#c9dcf3"/>
      </radialGradient>
    </defs>
    <rect width="952" height="1200" fill="var(--navy)"/>
    <path d="M0 292 C300 270 720 330 952 690 L952 1200 L0 1200 Z" fill="var(--sky)"/>
    <path d="M0 312 C300 292 700 352 952 712 L952 1200 L0 1200 Z" fill="url(#glow)"/>
  </svg>

  <h1 class="headline">TEPPICHREINIGUNG &amp;<br>TEPPICHREPARATUR -</h1>
  <p class="subline">KOSTENLOSE (GRATIS ) ABHOLUNG UND LIEFERUNG -</p>

  <div class="badge">
    <span class="badge-name">RVK</span>
    <span class="badge-sub">TEPPICHSERVICE<br>GMBH</span>
  </div>

  <div class="offer" style="top:436px;left:52px">
    <span class="offer-label" style="width:472px">Normalwäsche</span>
    <div class="offer-price" style="left:15px"><span class="old">19€</span><span class="jetzt">jetzt</span><span class="new">16,-€</span></div>
  </div>
  <div class="offer" style="top:656px">
    <span class="offer-label" style="width:390px;padding-left:36px">Vollwäsche</span>
    <div class="offer-price" style="left:28px;top:92px"><span class="old">27€</span><span class="jetzt">jetzt</span><span class="new">24,-€</span></div>
  </div>
  <div class="offer" style="top:856px">
    <span class="offer-label" style="width:498px;padding-left:38px">Seidenwäsche</span>
    <div class="offer-price" style="left:8px"><span class="old">49€</span><span class="jetzt">jetzt</span><span class="new">40,-€</span></div>
  </div>

  <p class="validity">Angebot gilt nur 5 Tage vom xx.xx.xx bis zum xx.xx.xx</p>

  <footer class="footer">
    <div class="hours"><b>Öffnungszeiten:</b><br>Mo- Fr&nbsp; 8.00 - 17:00 Uhr</div>
    <div class="address">Ahornweg 12<br>48231 Lindenfeld</div>
    <div class="phone">Tel.: 05372 / 58 204 36</div>
  </footer>
</div>
</body>
</html>
```